Vendra Q7 - DL Flyer

Flyer designed with the following points:

Retail Point of Sale
Hardware and Software
Highly customisable to suit your business
Free POS appraisal and Quotes
E-commerce Integrations with your existing website
Multiple Store Capability
One on one set up and support
100% Tax Deductable
From only $9.95 per week

1300 462 718
admin@vendraq7.com.au
www.vendraq7.com.au

```html
<!DOCTYPE html>
<html lang="en">
<head>
<meta charset="utf-8">
<title>Vendra Q7 – DL Flyer</title>
<link href="https://fonts.googleapis.com/css2?family=Open+Sans:ital,wght@0,400;0,600;0,700;0,800;1,600&family=Source+Sans+3:ital,wght@0,400;1,400&display=swap" rel="stylesheet">
<style>
  :root{
    --stage:#a3a6a9;
    --shadow:#6d6e70;
    --paper:#ffffff;
    --cyan:#1fa3dc;
    --sky:#86d3f3;
    --navy-a:#2b3590;
    --navy-b:#1c61b0;
    --navy:#1f3f8f;
    --ink:#1d1d2b;
    --price:#24407f;
  }
  *{box-sizing:border-box;margin:0;padding:0}
  html,body{width:1200px;height:1200px;overflow:hidden;background:var(--stage)}
  body{position:relative;font-family:"Source Sans 3",sans-serif;color:var(--ink)}
  .shadow{position:absolute;width:443px;height:901px;background:var(--shadow);top:168px}
  .flyer{position:absolute;top:150px;width:437px;height:900px;background:var(--paper);overflow:hidden}
  .flyer--front{left:144px}
  .flyer--back{left:655px}
  .brand{position:absolute;top:14px;left:0;width:100%;text-align:center;font-family:"Open Sans",sans-serif;font-weight:800;font-size:31px;letter-spacing:.5px;color:var(--cyan)}
  .ribbon{position:absolute;left:84px;width:269px;height:19px;background:linear-gradient(90deg,var(--navy-a),var(--navy-b));color:#fff;font-family:"Open Sans",sans-serif;font-weight:700;font-size:11px;letter-spacing:1.6px;text-align:center;line-height:19px;z-index:2}
  .ribbon--lg{font-size:13px}
  .hero-photo{position:absolute;top:68px;left:0;width:100%;height:292px;background:linear-gradient(135deg,#c9cfc4 0%,#6f7f86 35%,#3a4a5a 60%,#b7a58a 100%)}
  .rule{position:absolute;left:29px;width:378px;height:2px;background:var(--navy)}
  .tagline{position:absolute;top:386px;left:0;width:100%;text-align:center;font-family:"Open Sans",sans-serif;font-weight:700;font-size:24px;letter-spacing:4px;color:var(--cyan);padding-left:0}
  .headline{position:absolute;top:408px;left:0;width:100%;text-align:center;font-family:"Open Sans",sans-serif;font-weight:700;font-size:80px;line-height:80px;letter-spacing:12px;color:var(--cyan)}
  .body-copy{position:absolute;left:42px;width:353px;font-size:11.2px;line-height:14.3px;text-align:justify;color:var(--ink)}
  .services{position:absolute;top:686px;list-style:none;font-style:italic;font-size:11px;line-height:14px}
  .services li{position:relative;padding-left:12px;margin-bottom:4px}
  .services li::before{content:"";position:absolute;left:0;top:4px;width:5px;height:5px;border-radius:50%;background:var(--cyan)}
  .services--left{left:49px;width:160px}
  .services--right{left:227px;width:180px}
  .footer{position:absolute;left:0;top:830px;width:100%;height:70px;background:var(--cyan);color:#fff}
  .footer-brand{position:absolute;left:28px;top:15px;font-family:"Open Sans",sans-serif;font-weight:800;font-size:31px;color:#fff}
  .footer-divider{position:absolute;left:219px;top:7px;width:1px;height:46px;background:#fff}
  .contacts{position:absolute;left:234px;top:7px;list-style:none;font-size:9.5px;line-height:14px}
  .contacts li{display:flex;align-items:center;gap:10px}
  .contacts svg{width:11px;height:11px}
  .product-band{position:absolute;top:68px;left:0;width:100%;height:292px;background:var(--sky)}
  .product{position:absolute;width:102px;text-align:center;font-family:"Open Sans",sans-serif}
  .product-frame{width:102px;height:79px;background:#fff;padding:3px}
  .product-pic{width:100%;height:100%}
  .product-name{margin-top:5px;font-size:9px;letter-spacing:1px;line-height:12px;color:#fff;font-weight:600;text-transform:uppercase}
  .product-price{margin-top:3px;font-size:9.5px;letter-spacing:1px;font-weight:700;color:var(--price)}
  .package{position:absolute;width:166px;height:177px;border:1.5px solid var(--cyan);text-align:center;font-family:"Open Sans",sans-serif}
  .package-head{height:39px;background:var(--cyan);color:#fff;padding-top:4px}
  .package-title{font-weight:700;font-size:17px;letter-spacing:1.6px;line-height:19px;white-space:nowrap}
  .package-sub{font-style:italic;font-weight:600;font-size:8.5px;letter-spacing:1.3px}
  .price{margin-top:7px;color:var(--price);font-weight:700;font-size:17px;line-height:18px}
  .price sup{font-size:8px;vertical-align:8px}
  .per-week{font-size:8.5px;letter-spacing:.8px;margin-top:1px}
  .features{list-style:none;width:122px;margin:3px auto 0;font-size:8.5px;letter-spacing:.6px;color:var(--price)}
  .features li{display:flex;align-items:center;justify-content:center;gap:4px;border-bottom:1px solid var(--price);line-height:11.5px;white-space:nowrap}
  .features svg{width:7px;height:7px;flex:none}
  .buy{display:inline-block;margin-top:6px;width:68px;height:14px;line-height:14px;background:var(--cyan);color:#fff;font-size:8.5px;letter-spacing:1px}
  .tax{margin-top:3px;font-weight:600;font-size:10px;letter-spacing:1.2px;line-height:12px}
  .invoiced{font-size:8.5px;letter-spacing:.8px;line-height:10px}
</style>
</head>
<body>
<svg width="0" height="0" style="position:absolute">
  <defs>
    <symbol id="tick" viewBox="0 0 10 10"><circle cx="5" cy="5" r="4.2" fill="none" stroke="currentColor" stroke-width="1"/><path d="M3 5.2l1.4 1.4L7.2 3.8" fill="none" stroke="currentColor" stroke-width="1"/></symbol>
    <symbol id="i-phone" viewBox="0 0 12 12"><circle cx="6" cy="6" r="5.3" fill="none" stroke="#fff" stroke-width="1"/><path d="M4 3.3l1 1.4-.6.7a4 4 0 0 0 2.2 2.2l.7-.6 1.4 1-.6 1c-2.5-.2-4.6-2.3-4.8-4.8z" fill="#fff"/></symbol>
    <symbol id="i-mail" viewBox="0 0 12 12"><circle cx="6" cy="6" r="5.3" fill="none" stroke="#fff" stroke-width="1"/><rect x="3.3" y="4.2" width="5.4" height="3.8" fill="#fff"/><path d="M3.3 4.2L6 6.4l2.7-2.2" fill="none" stroke="var(--cyan)" stroke-width=".6"/></symbol>
    <symbol id="i-web" viewBox="0 0 12 12"><circle cx="6" cy="6" r="5.3" fill="none" stroke="#fff" stroke-width="1"/><circle cx="6" cy="6" r="3" fill="none" stroke="#fff" stroke-width=".7"/><path d="M3 6h6M6 3v6M6 3c-1.5 1.6-1.5 4.4 0 6M6 3c1.5 1.6 1.5 4.4 0 6" fill="none" stroke="#fff" stroke-width=".6"/></symbol>
  </defs>
</svg>

<div class="shadow" style="left:125px"></div>
<div class="shadow" style="left:636px"></div>

<!-- Front side -->
<section class="flyer flyer--front">
  <div class="brand">VENDRA Q7</div>
  <div class="ribbon" style="top:58px">LOREM IPSUM DOLOR SIT AMET</div>
  <div class="hero-photo" role="img" aria-label="Photo of hands tapping a touchscreen point-of-sale terminal at a shop counter"></div>
  <div class="rule" style="top:369px"></div>
  <div class="tagline">WE ARE AWESOME</div>
  <div class="headline">RETAIL</div>
  <div class="rule" style="top:486px"></div>

  <div class="ribbon ribbon--lg" style="top:519px">HOW WE WORK</div>
  <p class="body-copy" style="top:545px">Lorem ipsum dolor sit amet, consectetur adipiscing elit. Donec volutpat felis ac odio vulputate, vel scelerisque justo iaculis. Sed id blandit nulla. Proin vitae tellus placerat, euismod eros non, elementum diam. Nullam et ligula vel mi molestie dapibus sit amet sed mi. Vivamus feugiat ipsum in nisi volutpat, non varius lacus finibus. Nullam porta nulla et nisi blandit, ac facilisis eros lobortis. Proin porttitor neque at mauris pretium varius.</p>

  <div class="ribbon ribbon--lg" style="top:647px">OUR SERVICES</div>
  <ul class="services services--left">
    <li>Retail Point of Sale<br>Hardware and Software</li>
    <li>Highly customisable to<br>suit your business</li>
    <li>Free POS appraisal &amp; Quotes</li>
  </ul>
  <ul class="services services--right">
    <li>E-commerce Integrations<br>with your existing website</li>
    <li>Multiple Store Capability</li>
    <li>One on one set up and support</li>
    <li>100% Tax Deductable<br>From only $9.95 per week</li>
  </ul>

  <footer class="footer">
    <div class="footer-brand">VENDRA Q7</div>
    <div class="footer-divider"></div>
    <ul class="contacts">
      <li><svg><use href="#i-phone"/></svg>1300 462 718</li>
      <li><svg><use href="#i-mail"/></svg>admin@vendraq7.com.au</li>
      <li><svg><use href="#i-web"/></svg>www.vendraq7.com.au</li>
    </ul>
  </footer>
</section>

<!-- Back side -->
<section class="flyer flyer--back">
  <div class="brand">VENDRA Q7</div>
  <div class="product-band"></div>
  <div class="ribbon ribbon--lg" style="top:58px">PRODUCT LIST VENDRA Q7</div>

  <div class="product" style="left:46px;top:99px">
    <div class="product-frame"><div class="product-pic" style="background:#1f3f8f" role="img" aria-label="Service tile"></div></div>
    <div class="product-name">Kiosk<br>Assist</div><div class="product-price">$0.00</div>
  </div>
  <div class="product" style="left:167px;top:99px">
    <div class="product-frame"><div class="product-pic" style="background:radial-gradient(circle,#b9bcc0 0%,#fff 75%)" role="img" aria-label="Photo of a push lawn mower"></div></div>
    <div class="product-name">Lawn Mower<br>200 HP Tallis</div><div class="product-price">$499.00</div>
  </div>
  <div class="product" style="left:288px;top:99px">
    <div class="product-frame"><div class="product-pic" style="background:radial-gradient(circle,#d9372e 0%,#fff 75%)" role="img" aria-label="Photo of a red ride-on mower"></div></div>
    <div class="product-name">Ride On<br>Mower</div><div class="product-price">$1,950.00</div>
  </div>
  <div class="product" style="left:46px;top:227px">
    <div class="product-frame"><div class="product-pic" style="background:linear-gradient(135deg,#7a4a36,#b3734f 50%,#8aa05a)" role="img" aria-label="Photo of a grilled steak with salad"></div></div>
    <div class="product-name">Scotch Fillet</div><div class="product-price">$42.00</div>
  </div>
  <div class="product" style="left:167px;top:227px">
    <div class="product-frame"><div class="product-pic" style="background:radial-gradient(circle,#6c6f78 0%,#fff 60%)" role="img" aria-label="Photo of a desktop stapler"></div></div>
    <div class="product-name">Stapler</div><div class="product-price">$14.95</div>
  </div>
  <div class="product" style="left:288px;top:227px">
    <div class="product-frame"><div class="product-pic" style="background:radial-gradient(ellipse at center,#1b1b1b 0%,#fff 62%)" role="img" aria-label="Photo of a black summer dress"></div></div>
    <div class="product-name">Summer Dress</div><div class="product-price">$60.00</div>
  </div>

  <div class="ribbon ribbon--lg" style="top:363px">PRICE LIST VENDRA Q7</div>
  <p class="body-copy" style="top:386px;height:58px;overflow:hidden">Lorem ipsum dolor sit amet, consectetur adipiscing elit. Donec volutpat felis ac odio vulputate, vel scelerisque justo iaculis. Sed id blandit nulla. Proin vitae tellus placerat, euismod eros non, elementum diam. Nullam et ligula vel mi molestie dapibus sit amet sed mi. Vivamus feugiat ipsum in</p>

  <div class="package" style="left:34px;top:446px">
    <div class="package-head"><div class="package-title">SMALL RETAIL</div><div class="package-sub">SOFTWARE PACKAGE</div></div>
    <div class="price"><sup>$</sup> 9 <sup>95</sup></div>
    <div class="per-week">PER WEEK</div>
    <ul class="features"><li><svg><use href="#tick"/></svg>1-2 Staff Users</li><li><svg><use href="#tick"/></svg>1 Cash Register</li><li><svg><use href="#tick"/></svg>1 Store Location</li></ul>
    <span class="buy">BUY NOW</span>
    <div class="tax">100% TAX DEDUCTIBLE</div><div class="invoiced">(Invoiced Monthly)</div>
  </div>
  <div class="package" style="left:225px;top:446px">
    <div class="package-head"><div class="package-title">MEDIUM RETAIL</div><div class="package-sub">SOFTWARE PACKAGE</div></div>
    <div class="price"><sup>$</sup>17<sup>95</sup></div>
    <div class="per-week">PER WEEK</div>
    <ul class="features"><li><svg><use href="#tick"/></svg>3-8 Staff Users</li><li><svg><use href="#tick"/></svg>2-3 Cash Registers</li><li><svg><use href="#tick"/></svg>1 Store Location</li></ul>
    <span class="buy">BUY NOW</span>
    <div class="tax">100% TAX DEDUCTIBLE</div><div class="invoiced">(Invoiced Monthly)</div>
  </div>
  <div class="package" style="left:34px;top:641px">
    <div class="package-head"><div class="package-title">LARGE RETAIL</div><div class="package-sub">SOFTWARE PACKAGE</div></div>
    <div class="price"><sup>$</sup>34<sup>95</sup></div>
    <div class="per-week">PER WEEK</div>
    <ul class="features"><li><svg><use href="#tick"/></svg>8-20 Staff Users</li><li><svg><use href="#tick"/></svg>2-10 Cash Registers</li><li><svg><use href="#tick"/></svg>1 Store Location</li></ul>
    <span class="buy">BUY NOW</span>
    <div class="tax">100% TAX DEDUCTIBLE</div><div class="invoiced">(Invoiced Monthly)</div>
  </div>
  <div class="package" style="left:225px;top:641px">
    <div class="package-head"><div class="package-title">LARGE RETAIL</div><div class="package-sub">SOFTWARE PACKAGE</div></div>
    <div class="price"><sup>$</sup>49<sup>95</sup></div>
    <div class="per-week">PER WEEK</div>
    <ul class="features"><li><svg><use href="#tick"/></svg>20+ Staff Users</li><li><svg><use href="#tick"/></svg>10+ Cash Registers</li><li><svg><use href="#tick"/></svg>2-3 Store Locations</li></ul>
    <span class="buy">BUY NOW</span>
    <div class="tax">100% TAX DEDUCTIBLE</div><div class="invoiced">(Invoiced Monthly)</div>
  </div>

  <footer class="footer">
    <div class="footer-brand">VENDRA Q7</div>
    <div class="footer-divider"></div>
    <ul class="contacts">
      <li><svg><use href="#i-phone"/></svg>1300 462 718</li>
      <li><svg><use href="#i-mail"/></svg>admin@vendraq7.com.au</li>
      <li><svg><use href="#i-web"/></svg>www.vendraq7.com.au</li>
    </ul>
  </footer>
</section>
</body>
</html>
```